Storm Restoration Contractor needs a professional business card design

Looking for a professional business card design. Not looking for your cheapo MS Word standard ones that are readily available. Dont want it to be cookie cutter look like ones readily available online. We just recently changed our logo and want to freshen up all our documents. Our company handles restoring a property back to a pre-loss condition after a storm damages it. For example, wind, hail, flood, fire losses.

Target Market(s)

Property Owners, Homeowners, Property Owners, Commercial Property Owners, Property Management Companies, Hail and Wind Damaged Properties

Industry/Entity Type

Construction Company

Contact Information for Business Card

Brightline Facades
847-555-0193
847-555-0147 fax
www.brightlinefacades.example
info@brightlinefacades.example

Requirements
Must have
• Clean, Professional, fresh look
• Storm Restoration, Roofing, Siding, Windows
Nice to have
• If there is a way to incorporate storms that may be cool.

```html
<!DOCTYPE html>
<html lang="en">
<head>
<meta charset="utf-8">
<title>Brightline Facades – Business Card</title>
<link rel="stylesheet" href="https://fonts.googleapis.com/css2?family=Catamaran:wght@500;700&family=Oswald:wght@500&family=Tinos&display=swap">
<style>
  :root {
    --page-bg: #e4e6e9;
    --card-bg: #ffffff;
    --brand-blue: #1474c4;
    --blue-deep: #3566b8;
    --blue-light: #3a97d8;
    --fold-grey: #56585c;
    --fold-grey-light: #6d6f73;
    --ink: #3b3d40;
    --scene-tone: #cfe6f4;
  }
  * { margin: 0; padding: 0; box-sizing: border-box; }
  html, body {
    width: 1200px; height: 1200px; overflow: hidden;
    background: var(--page-bg);
  }
  .sheet { position: relative; width: 1200px; height: 1200px; }
  .card {
    position: absolute; left: 198px; width: 812px; height: 434px;
    background: var(--card-bg);
    box-shadow: 0 6px 18px rgba(0,0,0,0.18);
    overflow: hidden;
  }
  .card--front { top: 132px; }
  .card--back { top: 626px; }
  .card svg { display: block; width: 812px; height: 434px; }
  .text-sans { font-family: "Catamaran", sans-serif; }
  .text-condensed { font-family: "Oswald", sans-serif; }
  .text-serif { font-family: "Tinos", serif; }
</style>
</head>
<body>
<main class="sheet">

  <section class="card card--front" aria-label="Business card front">
    <svg viewBox="0 0 1015 542" xmlns="http://www.w3.org/2000/svg">
      <defs>
        <linearGradient id="frontBlue" x1="0" y1="0" x2="1" y2="1">
          <stop offset="0" stop-color="#1b6fc3"/>
          <stop offset="1" stop-color="#3a97d8"/>
        </linearGradient>
        <linearGradient id="frontBlueBR" x1="0" y1="1" x2="1" y2="0">
          <stop offset="0" stop-color="#3a97d8"/>
          <stop offset="1" stop-color="#3566b8"/>
        </linearGradient>
        <linearGradient id="sceneFade" x1="0" y1="0" x2="1" y2="0">
          <stop offset="0" stop-color="#cfe6f4" stop-opacity="0"/>
          <stop offset="0.55" stop-color="#cfe6f4" stop-opacity="0.7"/>
          <stop offset="1" stop-color="#cfe6f4" stop-opacity="0"/>
        </linearGradient>
      </defs>

      <!-- illustration area -->
      <rect role="img" aria-label="Faint illustration of a house with a light blue roof" x="240" y="360" width="720" height="182" fill="url(#sceneFade)"/>

      <!-- top-left folded corner -->
      <polygon class="fold-blue" points="0,0 312,0 265,110 120,87 0,222" fill="url(#frontBlue)"/>
      <polygon class="fold-grey" points="120,87 265,110 312,0 0,310 0,222" fill="var(--fold-grey)"/>

      <!-- bottom-right folded corner -->
      <polygon class="fold-blue" points="710,542 1015,325 1015,542" fill="url(#frontBlueBR)"/>
      <polygon class="fold-grey" points="950,370 1015,325 990,398" fill="var(--fold-grey-light)"/>

      <!-- brand block -->
      <circle cx="225" cy="292" r="98" fill="none" stroke="var(--brand-blue)" stroke-width="14"/>
      <rect x="350" y="188" width="4" height="210" fill="var(--brand-blue)"/>
      <text class="text-sans" x="380" y="296" font-size="92" font-weight="700" fill="var(--brand-blue)">BRIGHTLINE</text>
      <text class="text-sans" x="380" y="368" font-size="92" font-weight="700" fill="var(--brand-blue)">FACADES</text>

      <text class="text-sans" x="917" y="38" text-anchor="end" font-size="26" font-weight="500" fill="var(--ink)" letter-spacing="1">www.brightlinefacades.example</text>
      <text class="text-sans" x="196" y="530" font-size="26" font-weight="500" fill="var(--ink)" letter-spacing="1">info@brightlinefacades.example</text>
    </svg>
  </section>

  <section class="card card--back" aria-label="Business card back">
    <svg viewBox="0 0 1015 542" xmlns="http://www.w3.org/2000/svg">
      <defs>
        <linearGradient id="backBlue" x1="0" y1="0" x2="0.6" y2="1">
          <stop offset="0" stop-color="#3a97d8"/>
          <stop offset="0.55" stop-color="#2f88cf"/>
          <stop offset="1" stop-color="#3566b8"/>
        </linearGradient>
        <linearGradient id="sceneFadeBack" x1="0" y1="0" x2="1" y2="0">
          <stop offset="0" stop-color="#cfe6f4" stop-opacity="0"/>
          <stop offset="0.55" stop-color="#cfe6f4" stop-opacity="0.7"/>
          <stop offset="1" stop-color="#cfe6f4" stop-opacity="0"/>
        </linearGradient>
      </defs>

      <!-- illustration area -->
      <rect role="img" aria-label="Faint illustration of a house with a light blue roof" x="0" y="380" width="600" height="162" fill="url(#sceneFadeBack)"/>

      <!-- blue panel with folds -->
      <polygon class="panel-blue" points="685,0 1015,0 1015,542 567,542 635,350 425,240 490,90" fill="url(#backBlue)"/>
      <polygon class="fold-grey" points="425,240 635,350 600,430" fill="var(--fold-grey)"/>
      <polygon class="fold-grey" points="905,425 1015,452 1015,542 962,542" fill="var(--fold-grey-light)"/>

      <!-- brand block -->
      <circle cx="230" cy="160" r="80" fill="none" stroke="var(--brand-blue)" stroke-width="13"/>
      <text class="text-sans" x="230" y="278" text-anchor="middle" font-size="34" font-weight="700" fill="var(--brand-blue)" letter-spacing="2">BRIGHTLINE FACADES</text>

      <!-- contact details -->
      <text class="text-sans" x="982" y="115" text-anchor="end" font-size="44" font-weight="700" fill="#ffffff">Brightline Facades</text>
      <text class="text-condensed" x="975" y="180" text-anchor="end" font-size="42" font-weight="500" fill="#ffffff">Ph : 847-555-0193</text>
      <text class="text-condensed" x="975" y="237" text-anchor="end" font-size="42" font-weight="500" fill="#ffffff">Fax : 847-555-0147</text>
      <text class="text-serif" x="980" y="282" text-anchor="end" font-size="33" fill="#ffffff">info@brightlinefacades.example</text>

      <text class="text-sans" x="96" y="530" font-size="26" font-weight="500" fill="var(--ink)" letter-spacing="1">www.brightlinefacades.example</text>
    </svg>
  </section>

</main>
</body>
</html>
```